Letter design, envelope design, and more

Hello, we the Varlo Gmbh are looking for our shop. Letter C5. Design does not have to be like a business card, so it can have straight lines. Only the color is important. The logo is the text under VaRLo omit.It should not be playful but Profesionel

Font styles to use
Sans Serif

Colors
0555a3
3176b5
85abd2
85cae6
34a7d8
0792cd
cee9f5
cfdfed
000000

Requirements
Must have
• Color like business card, Please, with the text under VaRLo, Correct address Benkelstr. 4 Zip code 9512 Goldach, as well as Couvert Without addressing only design and logo with VaRlo
Nice to have
• more writing articles
Should not have
• Not too colored, Text under VaRLo, bright colors

```html
<!DOCTYPE html>
<html lang="de">
<head>
<meta charset="utf-8">
<title>Varlo Gmbh – Briefpapier und Couvert</title>
<link href="https://fonts.googleapis.com/css2?family=Open+Sans:wght@400;600&display=swap" rel="stylesheet">
<style>
  :root {
    --stage: #cbcbcb;
    --paper: #ffffff;
    --band-deep: #0555a3;
    --band-mid: #3176b5;
    --band-light: #85abd2;
    --brand: #0555a3;
    --contact: #cee9f5;
  }
  * { margin: 0; padding: 0; box-sizing: border-box; }
  html, body { width: 1200px; height: 1200px; overflow: hidden; }
  body {
    background: var(--stage);
    font-family: "Open Sans", Arial, sans-serif;
    position: relative;
  }
  .sheet {
    position: absolute;
    background: var(--paper);
    box-shadow: 0 2px 6px rgba(0,0,0,.28);
    overflow: hidden;
  }
  .letter-wave   { left: 140px; top: 30px;  width: 445px; height: 628px; }
  .letter-band   { left: 614px; top: 30px;  width: 445px; height: 628px; }
  .envelope-wave { left: 100px; top: 797px; width: 485px; height: 343px; }
  .envelope-band { left: 614px; top: 797px; width: 486px; height: 343px; }
  .sheet svg.footer-art { position: absolute; left: 0; top: 0; width: 100%; height: 100%; }

  .brand {
    position: absolute;
    display: flex;
    align-items: center;
    color: var(--brand);
    font-weight: 600;
    white-space: nowrap;
  }
  .brand-square { background: var(--brand); flex: none; }
  .brand-small { left: 40px; top: 39px; font-size: 16px; gap: 6px; }
  .brand-small .brand-square { width: 22px; height: 22px; }
  .brand-large { font-size: 30px; gap: 12px; }
  .brand-large .brand-square { width: 56px; height: 56px; }
  .envelope-wave .brand-large { left: 196px; top: 113px; }
  .envelope-band .brand-large { left: 196px; top: 107px; }

  .contact-row {
    position: absolute;
    display: flex;
    color: var(--contact);
    font-size: 5.6px;
    line-height: 1.25;
  }
  .letter-wave .contact-row { left: 140px; top: 601px; }
  .letter-band .contact-row { left: 140px; top: 607px; }
  .contact-item { display: flex; align-items: center; gap: 3px; width: 72px; }
  .contact-item svg { width: 9px; height: 9px; flex: none; }
</style>
</head>
<body>

<section class="sheet letter-wave" aria-label="Briefbogen mit geschwungenem Fuss">
  <div class="brand brand-small"><span class="brand-square"></span>VARLO GMBH</div>
  <svg class="footer-art" viewBox="0 0 445 628" preserveAspectRatio="none" aria-hidden="true">
    <path d="M0,568 C140,592 300,602 445,572 L445,628 L0,628 Z" fill="var(--band-light)"/>
    <path d="M0,584 C90,598 170,604 240,602 C140,612 60,620 0,628 Z" fill="var(--band-mid)"/>
    <path d="M0,618 C160,590 330,598 445,568 L445,628 L0,628 Z" fill="var(--band-deep)"/>
  </svg>
  <div class="contact-row">
    <div class="contact-item"><svg viewBox="0 0 10 10"><circle cx="5" cy="5" r="4.4" fill="none" stroke="currentColor" stroke-width=".7"/><path d="M3.4,3 L4.2,2.8 4.6,4 4,4.4 Q4.6,5.6 5.6,6 L6,5.4 7.2,5.8 7,6.6 Q4,6.8 3.4,3 Z" fill="currentColor"/></svg>+41 71 555 20 40</div>
    <div class="contact-item"><svg viewBox="0 0 10 10"><circle cx="5" cy="5" r="4.4" fill="none" stroke="currentColor" stroke-width=".7"/><path d="M3,3.5 L7,3.5 7,6.5 3,6.5 Z M3,3.5 L5,5.2 7,3.5" fill="none" stroke="currentColor" stroke-width=".6"/></svg>info@varlo.ch</div>
    <div class="contact-item"><svg viewBox="0 0 10 10"><circle cx="5" cy="5" r="4.4" fill="none" stroke="currentColor" stroke-width=".7"/><path d="M5,7.4 C3.6,5.6 3.4,5 3.4,4.4 A1.6,1.6 0 0 1 6.6,4.4 C6.6,5 6.4,5.6 5,7.4 Z" fill="currentColor"/></svg><span>Benkelstr. 4<br>9512 Goldach</span></div>
    <div class="contact-item"><svg viewBox="0 0 10 10"><circle cx="5" cy="5" r="4.4" fill="none" stroke="currentColor" stroke-width=".7"/><path d="M3,5.2 L7,3 5,7 4.6,5.4 Z" fill="currentColor"/></svg>www.varlo.ch</div>
  </div>
</section>

<section class="sheet letter-band" aria-label="Briefbogen mit geradem Fussband">
  <div class="brand brand-small"><span class="brand-square"></span>VARLO GMBH</div>
  <svg class="footer-art" viewBox="0 0 445 628" preserveAspectRatio="none" aria-hidden="true">
    <defs>
      <linearGradient id="bandFadeA" x1="0" x2="1">
        <stop offset="0" stop-color="var(--band-light)"/><stop offset="1" stop-color="var(--band-mid)"/>
      </linearGradient>
    </defs>
    <rect x="0" y="592" width="445" height="3" fill="url(#bandFadeA)"/>
    <rect x="0" y="595" width="445" height="2" fill="var(--band-mid)"/>
    <rect x="0" y="597" width="445" height="31" fill="var(--band-deep)"/>
  </svg>
  <div class="contact-row">
    <div class="contact-item"><svg viewBox="0 0 10 10"><circle cx="5" cy="5" r="4.4" fill="none" stroke="currentColor" stroke-width=".7"/><path d="M3.4,3 L4.2,2.8 4.6,4 4,4.4 Q4.6,5.6 5.6,6 L6,5.4 7.2,5.8 7,6.6 Q4,6.8 3.4,3 Z" fill="currentColor"/></svg>+41 71 555 20 40</div>
    <div class="contact-item"><svg viewBox="0 0 10 10"><circle cx="5" cy="5" r="4.4" fill="none" stroke="currentColor" stroke-width=".7"/><path d="M3,3.5 L7,3.5 7,6.5 3,6.5 Z M3,3.5 L5,5.2 7,3.5" fill="none" stroke="currentColor" stroke-width=".6"/></svg>info@varlo.ch</div>
    <div class="contact-item"><svg viewBox="0 0 10 10"><circle cx="5" cy="5" r="4.4" fill="none" stroke="currentColor" stroke-width=".7"/><path d="M5,7.4 C3.6,5.6 3.4,5 3.4,4.4 A1.6,1.6 0 0 1 6.6,4.4 C6.6,5 6.4,5.6 5,7.4 Z" fill="currentColor"/></svg><span>Benkelstr. 4<br>9512 Goldach</span></div>
    <div class="contact-item"><svg viewBox="0 0 10 10"><circle cx="5" cy="5" r="4.4" fill="none" stroke="currentColor" stroke-width=".7"/><path d="M3,5.2 L7,3 5,7 4.6,5.4 Z" fill="currentColor"/></svg>www.varlo.ch</div>
  </div>
</section>

<section class="sheet envelope-wave" aria-label="Couvert mit geschwungenem Fuss">
  <div class="brand brand-large"><span class="brand-square"></span>VARLO GMBH</div>
  <svg class="footer-art" viewBox="0 0 485 343" preserveAspectRatio="none" aria-hidden="true">
    <path d="M0,255 C160,300 340,300 485,254 L485,343 L0,343 Z" fill="var(--band-light)"/>
    <path d="M0,272 C80,290 150,296 220,296 C130,304 60,314 0,322 Z" fill="var(--band-mid)"/>
    <path d="M0,318 C170,282 360,296 485,254 L485,343 L0,343 Z" fill="var(--band-deep)"/>
  </svg>
</section>

<section class="sheet envelope-band" aria-label="Couvert mit geradem Fussband">
  <div class="brand brand-large"><span class="brand-square"></span>VARLO GMBH</div>
  <svg class="footer-art" viewBox="0 0 486 343" preserveAspectRatio="none" aria-hidden="true">
    <defs>
      <linearGradient id="bandFadeB" x1="0" x2="1">
        <stop offset="0" stop-color="var(--band-light)"/><stop offset=".85" stop-color="var(--band-mid)"/><stop offset="1" stop-color="var(--band-mid)" stop-opacity="0"/>
      </linearGradient>
    </defs>
    <rect x="0" y="265" width="486" height="6" fill="url(#bandFadeB)"/>
    <rect x="0" y="271" width="486" height="5" fill="url(#bandFadeB)" opacity=".6"/>
    <rect x="0" y="276" width="486" height="4" fill="var(--band-deep)" opacity=".85"/>
    <rect x="0" y="280" width="486" height="63" fill="var(--band-deep)"/>
  </svg>
</section>

</body>
</html>
```